BRAVEN POWERLINE SERVICES needs a vibrant design for electrical contracting work.

I require a card design for my own electrical contracting business. I will be doing a lot of domestic and commercial work, including things such as repairs, maintenance, lighting, installations and various others. LED lighting and energy efficiency will be a big part of my business. I wish not to have childish pictures such as light bulbs in the design, but rather a smart and modern looking card which incorporates my logo colours and perhaps the same lighting strike within the faded background of the card.

Target Market(s)

Residential and Commercial property owners.

Industry/Entity Type

Electrical

Contact Information for Business Card

Dalen Voskic
EC40923
Phone Number: 0417 358 942
Email: dalen@bravenpowerline.com

Font styles to use
Serif
Sans Serif

Requirements
Must have
• My Logo and associated colours.
Nice to have
• Some form of shapes splitting the card into different colours related to the colours of my logo. Electric Blue, Silver/Grey and White.
Should not have
• Childish pictures and symbols such as light bulbs.

```html
<!DOCTYPE html>
<html lang="en">
<head>
<meta charset="utf-8">
<title>Braven Powerline Services – Business Card</title>
<link rel="stylesheet" href="https://fonts.googleapis.com/css2?family=Lato:wght@400;700;900&family=Libre+Baskerville:wght@400;700&display=swap">
<style>
  :root{
    --bg:#2b2b2b;
    --card-white:#f4f4f4;
    --card-shade:#e2e2e2;
    --panel:#5a5a5a;
    --panel-dark:#474747;
    --divider:#3a3a3a;
    --electric:#1f2fe0;
    --electric-soft:#b9bff2;
    --silver:#c9c9c9;
    --text-light:#eaeaea;
    --label:#f2f2f2;
  }
  *{box-sizing:border-box;margin:0;padding:0}
  html,body{width:1200px;height:873px;overflow:hidden;background:var(--bg)}
  .canvas{position:relative;width:1200px;height:873px}
  .card{
    position:absolute;left:290px;width:620px;height:354px;border-radius:22px;
    overflow:hidden;background:linear-gradient(135deg,var(--card-white),var(--card-shade));
    box-shadow:0 14px 30px rgba(0,0,0,.55);
  }
  .card--front{top:52px}
  .card--back{top:466px}

  .brand{display:flex;align-items:center;gap:14px}
  .brand__dot{width:46px;height:46px;border-radius:50%;background:var(--silver);flex:none}
  .brand__name{
    font-family:"Lato",sans-serif;font-weight:900;color:var(--electric);
    text-transform:uppercase;line-height:1.05;letter-spacing:.5px;
  }
  .card--front .brand{position:absolute;left:50%;top:50%;transform:translate(-50%,-50%)}
  .card--front .brand__name{font-size:34px}
  .card--front .faint-ring{
    position:absolute;left:50%;top:50%;width:230px;height:230px;margin:-115px 0 0 -115px;
    border-radius:50%;background:rgba(185,191,242,.28);
  }

  .back__logo-side{position:absolute;left:0;top:0;width:360px;height:100%}
  .back__logo-side .brand{position:absolute;left:34px;top:50%;transform:translateY(-50%)}
  .back__logo-side .brand__name{font-size:27px}
  .back__divider{position:absolute;left:360px;top:0;width:12px;height:100%;background:var(--divider)}
  .back__panel{
    position:absolute;left:372px;top:0;right:0;height:100%;
    background:linear-gradient(160deg,var(--panel),var(--panel-dark));
    padding:18px 14px 0 12px;color:var(--text-light);
  }
  .back__panel .faint-ring{
    position:absolute;left:70px;top:120px;width:160px;height:160px;border-radius:50%;
    background:rgba(255,255,255,.07);
  }
  .label{
    display:inline-block;background:var(--label);color:var(--electric);
    font-family:"Libre Baskerville",serif;font-size:17px;letter-spacing:1px;
    padding:3px 10px 2px;text-transform:uppercase;position:relative;
  }
  .contact{list-style:none;margin:10px 0 0;font-family:"Lato",sans-serif;font-size:13.5px;position:relative}
  .contact li{display:flex;gap:8px;align-items:flex-start;margin-bottom:5px;line-height:1.3}
  .contact svg{flex:none;margin-top:2px}
  .services-title{margin:10px 0 0 46px}
  .services{margin:12px 0 0 26px;font-family:"Lato",sans-serif;font-size:16px;color:#fff;position:relative}
  .services li{margin-bottom:6px}
  .services li::marker{color:#fff}
</style>
</head>
<body>
<main class="canvas">

  <section class="card card--front" aria-label="Card front">
    <div class="faint-ring" aria-hidden="true"></div>
    <div class="brand">
      <span class="brand__dot" aria-hidden="true"></span>
      <span class="brand__name">Braven Powerline<br>Services</span>
    </div>
  </section>

  <section class="card card--back" aria-label="Card back">
    <div class="back__logo-side">
      <div class="brand">
        <span class="brand__dot" aria-hidden="true"></span>
        <span class="brand__name">Braven Powerline<br>Services</span>
      </div>
    </div>
    <div class="back__divider" aria-hidden="true"></div>
    <div class="back__panel">
      <div class="faint-ring" aria-hidden="true"></div>
      <h1 class="label">Dalen Voskic</h1>
      <ul class="contact">
        <li>
          <svg width="12" height="14" viewBox="0 0 12 14" aria-hidden="true"><rect x="2" y="0.5" width="8" height="13" rx="1.5" fill="none" stroke="#eaeaea" stroke-width="1.3"/><circle cx="6" cy="11" r="0.9" fill="#eaeaea"/></svg>
          <span>0417 358 942</span>
        </li>
        <li>
          <svg width="14" height="12" viewBox="0 0 14 12" aria-hidden="true"><rect x="0.5" y="1.5" width="13" height="9" fill="#eaeaea"/><path d="M0.5 1.5 L7 7 L13.5 1.5" fill="none" stroke="#555" stroke-width="1.2"/></svg>
          <span>dalen@bravenpowerline.com</span>
        </li>
        <li>
          <svg width="12" height="14" viewBox="0 0 12 14" aria-hidden="true"><path d="M6 13.5 C2 8.5 1 6.8 1 5 A5 5 0 0 1 11 5 C11 6.8 10 8.5 6 13.5Z" fill="#eaeaea"/><circle cx="6" cy="5" r="1.8" fill="#555"/></svg>
          <span>2480 W. Harbor Road 9<br>Fairview, Fl 33187</span>
        </li>
      </ul>
      <h2 class="label services-title">My Services</h2>
      <ul class="services">
        <li>Repairs</li>
        <li>Maintenance</li>
        <li>Installations</li>
        <li>LED lighting</li>
        <li>Energy Efficiency</li>
      </ul>
    </div>
  </section>

</main>
</body>
</html>
```